Van wrap design for 2014 Brevik T360 Commercial Van

We are launching a maintenance division for our property company and have bought a new van to advertise our maintenance company. We will be advertising to property owners, the general public etc. our services.
We wish the text to read: Maintenance Division - remodels, plumbing & electrical.

• Both images attached

```html
<!DOCTYPE html>
<html lang="en">
<head>
<meta charset="utf-8">
<title>Maintenance Division – Brevik T360 Van Wrap</title>
<link rel="stylesheet" href="https://fonts.googleapis.com/css2?family=Roboto+Condensed:wght@700&display=swap">
<style>
  :root {
    --canvas: #f2f2f2;
    --van-body: #ffffff;
    --van-edge: #c9c9c9;
    --ink: #333333;
    --ink-soft: #5a5a5a;
    --band: #8c8c8c;
    --photo-light: #6f8ea6;
    --photo-dark: #2b3445;
  }
  html, body {
    margin: 0;
    padding: 0;
    width: 1200px;
    height: 1200px;
    overflow: hidden;
    background: var(--canvas);
  }
  .canvas {
    position: relative;
    width: 1200px;
    height: 1200px;
  }
  .van-side {
    position: absolute;
    left: 0;
    top: 0;
  }
  .wrap-photo {
    position: absolute;
    left: 134px;
    top: 382px;
    width: 312px;
    height: 300px;
    border-radius: 34px 0 0 12px;
    background: linear-gradient(160deg, var(--photo-light) 0%, #4c6479 45%, var(--photo-dark) 100%);
  }
  .wrap-band {
    position: absolute;
    left: 446px;
    top: 382px;
    width: 24px;
    height: 300px;
    background: var(--band);
  }
  .headline {
    position: absolute;
    left: 485px;
    top: 436px;
    margin: 0;
    font-family: "Roboto Condensed", "Arial Narrow", sans-serif;
    font-weight: 700;
    font-size: 36px;
    line-height: 1.15;
    color: var(--ink);
    text-transform: uppercase;
    letter-spacing: 0.3px;
  }
  .services {
    position: absolute;
    left: 487px;
    top: 556px;
    margin: 0;
    font-family: "Roboto Condensed", "Arial Narrow", sans-serif;
    font-weight: 700;
    font-size: 21px;
    line-height: 1.3;
    color: var(--ink-soft);
    text-transform: uppercase;
  }
  .brand {
    position: absolute;
    left: 776px;
    top: 578px;
    display: flex;
    align-items: center;
    gap: 10px;
    font-family: "Roboto Condensed", "Arial Narrow", sans-serif;
    font-weight: 700;
    font-size: 18px;
    line-height: 1;
    color: var(--ink);
  }
  .brand-mark {
    width: 18px;
    height: 18px;
    background: var(--ink);
    flex: none;
  }
</style>
</head>
<body>
<main class="canvas">
  <svg class="van-side" width="1200" height="1200" viewBox="0 0 1200 1200" aria-hidden="true">
    <path d="M120 420 Q124 378 170 376 L870 376 Q900 378 930 420 L990 520 Q1120 540 1130 590 L1130 670 Q1128 690 1100 690 L120 690 Q104 690 104 672 Z"
          fill="var(--van-body)" stroke="var(--van-edge)" stroke-width="2"/>
    <path d="M760 400 L890 400 L940 490 L760 490 Z" fill="none" stroke="var(--van-edge)" stroke-width="2"/>
    <line x1="590" y1="384" x2="590" y2="684" stroke="var(--van-edge)" stroke-width="2"/>
    <line x1="742" y1="384" x2="742" y2="684" stroke="var(--van-edge)" stroke-width="2"/>
  </svg>

  <div class="wrap-photo" role="img" aria-label="Photo of the two company founders in suits standing in front of a blue house"></div>
  <div class="wrap-band"></div>

  <h1 class="headline">Maintenance<br>Division</h1>
  <p class="services">Remodels,<br>Plumbing &amp; Electrical</p>

  <div class="brand">
    <span class="brand-mark"></span>
    <span class="brand-name">Halden Residential</span>
  </div>
</main>
</body>
</html>
```